skincare creams for tired moms

I need a package and a logo design for a skincare company based in California called Lumen Petal. I make day and night cream, under eye cream, and body lotion. The first product I plan to launch is an under eye cream. It does not have to be in these colors but I do teals, greens, black, and cobalt blue.

The package is going to either be in a box or a bag. Either way I go it will be like a gift box or bag. The design should make the person feel like they are getting something special and luxurious just for them.

I have small kids and it is really difficult to find a chunk of time to myself to update or review.

Target Market(s)

mainly first time moms. I am making an under eye cream that does not use retinol but is still powerful enough to get rid of bags and dark circles.

Industry/Entity Type

Cosmetics

Logo Text

The package and logo should incorporate the name Lumen Petal.

Font styles to use
Decorative
Script

Colors

Designer to choose colors to be used in the design.

Requirements
Nice to have
• maybe focus more on Petal instead of Lumen. Also incorporate plants or flowers
Should not have
• not a huge fan of pink

```html
<!DOCTYPE html>
<html lang="en">
<head>
<meta charset="utf-8">
<title>Lumen Petal — Under Eye Cream Package</title>
<link href="https://fonts.googleapis.com/css2?family=Cinzel:wght@400;600&family=EB+Garamond:wght@400&display=swap" rel="stylesheet">
<style>
  :root {
    --teal: #1f8c96;
    --teal-deep: #17727c;
    --leaf: #7cb342;
    --leaf-soft: #a5cf6a;
    --paper: #ffffff;
    --backdrop: #f1f2f2;
    --side: #f7f7f7;
    --rule: #d9dcdc;
  }
  * { box-sizing: border-box; margin: 0; padding: 0; }
  html, body {
    width: 1200px; height: 1200px; overflow: hidden;
    background: var(--backdrop);
  }
  .canvas {
    position: relative; width: 1200px; height: 1200px;
    display: flex; justify-content: center; align-items: center;
  }
  .carton {
    display: flex; height: 1040px;
    box-shadow: 0 10px 40px rgba(0,0,0,0.08);
  }
  .side-panel {
    width: 260px; background: var(--side);
    border-right: 1px solid var(--rule);
    padding: 90px 34px;
    display: flex; flex-direction: column; justify-content: space-between;
    font-family: "EB Garamond", Georgia, serif;
    color: var(--teal); font-size: 17px; line-height: 1.5; text-align: center;
  }
  .side-divider { display: block; width: 140px; height: 12px; margin: 0 auto; }
  .front-panel {
    width: 460px; background: var(--paper);
    display: flex; flex-direction: column; align-items: center;
    padding-top: 70px;
  }
  .wordmark {
    font-family: "Cinzel", Georgia, serif; font-weight: 600;
    color: var(--teal); text-align: center; line-height: 0.95;
  }
  .wordmark-primary { display: block; font-size: 92px; letter-spacing: 2px; }
  .wordmark-secondary { display: block; font-size: 64px; letter-spacing: 4px; }
  .botanical-helix {
    width: 230px; height: 560px; margin-top: 40px;
    background: linear-gradient(160deg, var(--leaf-soft) 0%, var(--leaf) 40%, var(--teal) 75%, var(--teal-deep) 100%);
    border-radius: 115px;
    opacity: 0.9;
  }
  .product-band {
    margin-top: 26px; width: 300px; background: var(--leaf);
    color: var(--paper); text-align: center;
    font-family: "Cinzel", Georgia, serif; padding: 10px 0 8px;
  }
  .product-band .line-small { display: block; font-size: 30px; letter-spacing: 2px; }
  .product-band .line-large { display: block; font-size: 50px; line-height: 1; letter-spacing: 1px; }
  .net-volume {
    margin-top: 18px; font-family: "Cinzel", Georgia, serif;
    color: var(--teal); font-size: 28px; letter-spacing: 1px;
  }
</style>
</head>
<body>
<main class="canvas">
  <section class="carton">
    <aside class="side-panel">
      <p class="side-copy">A gentle under eye cream made for tired mothers. Without retinol, it softens dark circles and eases puffiness while you rest.</p>
      <svg class="side-divider" viewBox="0 0 140 12" aria-hidden="true">
        <line x1="4" y1="6" x2="136" y2="6" stroke="#7cb342" stroke-width="1.5"/>
        <circle cx="4" cy="6" r="3" fill="#7cb342"/>
        <circle cx="136" cy="6" r="3" fill="#7cb342"/>
      </svg>
      <p class="side-copy">Apply a small drop each evening. Pat lightly beneath the eye with your ring finger until fully absorbed.</p>
    </aside>
    <article class="front-panel">
      <h1 class="wordmark">
        <span class="wordmark-primary">Lumen</span>
        <span class="wordmark-secondary">Petal</span>
      </h1>
      <div class="botanical-helix" role="img" aria-label="Illustration of a teal double helix entwined with green leafy vines and flowers"></div>
      <div class="product-band">
        <span class="line-small">Under Eye</span>
        <span class="line-large">Cream</span>
      </div>
      <p class="net-volume">0.5 oz</p>
    </article>
  </section>
</main>
</body>
</html>
```